Larkmoor Dental Center Specials/Offers

Take the advertisement pic (LABELED ADVERTISEMENT) and make it look "professional in appearance" using the logo and color scheme of Larkmoor Dental Center. The Phone number should be 614-382-2096. I want the same content, different background, professional looking document. I want it to be a 12"x12" document. High resolution files should include .PDF, .JPG and .AI. Any or all documents can be used for colors and overall scheme. I would like to have the overall colors include the main blue color from the file 4db749b4ef4c5e0717512bf7eb26bf54 and include the brown "swoosh" somewhere through/on the final document. Stock files of smiling young families can be used but not required. I am on a tight time-line and have placed 5 days as the deadline, but I will pick my favorite in as little as 2-3 days if I can get a good product. Again ALL the info from the Advertisement document should be included on the final product. Use any or all of the uploaded files for assistance. You can also visit our website for more info: www.larkmoordentalcenter.example Thanks

```html
<!DOCTYPE html>
<html lang="en">
<head>
<meta charset="utf-8">
<title>Larkmoor Dental Center – Specials</title>
<link rel="stylesheet" href="https://fonts.googleapis.com/css2?family=Oswald:wght@600;700&family=Archivo:ital,wght@0,700;0,800;0,900;1,800&family=Questrial&display=swap">
<style>
  :root{
    --teal-dark:#1f4a56;
    --steel:#5b8194;
    --steel-deep:#3f6678;
    --steel-light:#8fb0c0;
    --brown:#5a4840;
    --grey:#bdbdbd;
    --grey-light:#d9d9d9;
    --white:#ffffff;
    --ink:#2b3a42;
  }
  *{box-sizing:border-box;margin:0;padding:0}
  html,body{width:1151px;height:1200px;overflow:hidden;background:var(--white)}
  .ad{position:relative;width:1151px;height:1200px;overflow:hidden;font-family:"Archivo",Arial,sans-serif}
  .ad__backdrop{position:absolute;inset:0;width:1151px;height:1200px}
  .block{position:absolute}

  /* insurance */
  .providers{left:10px;top:10px;width:500px;color:var(--steel);font-family:"Oswald",sans-serif;text-align:center}
  .providers__title{font-size:46px;font-weight:700;line-height:1;text-shadow:1px 1px 0 var(--steel-deep),2px 3px 3px rgba(0,0,0,.3);text-align:left}
  .providers__list{font-size:23px;font-weight:600;line-height:1.15;margin-top:4px;text-shadow:1px 1px 1px rgba(0,0,0,.2);margin-left:-30px}
  .providers__list--gap{margin-top:20px}
  .providers__note{font-size:18px;font-weight:600;margin-left:-30px}

  /* referral cards */
  .referral{left:40px;top:183px;width:270px;height:260px}
  .referral__card{position:absolute;width:230px;height:212px;background:var(--steel);border:2px solid var(--white);box-shadow:2px 2px 4px rgba(0,0,0,.3)}
  .referral__card:nth-child(1){left:0;top:0}
  .referral__card:nth-child(2){left:18px;top:18px}
  .referral__card--front{left:36px;top:36px;width:234px;height:224px;border-radius:0 0 60px 0/0 0 30px 0;display:flex;flex-direction:column;align-items:center;justify-content:center;font-family:"Oswald",sans-serif;color:var(--white);text-shadow:1px 1px 0 var(--ink),2px 2px 2px rgba(0,0,0,.5);line-height:1.12;text-align:center}
  .referral__lead{font-size:40px;font-weight:700}
  .referral__word{font-size:36px;font-weight:600}

  /* new patients */
  .newpatients{left:620px;top:8px;width:520px;color:var(--white);text-align:center;font-weight:800;text-shadow:2px 2px 3px rgba(0,0,0,.6)}
  .newpatients__title{font-size:47px;font-weight:900;line-height:1.05}
  .newpatients__item{font-size:31px;line-height:1.12}
  .newpatients__note{font-size:16px;font-weight:700;margin-top:6px;padding-left:40px}

  /* starburst */
  .burst{left:805px;top:218px;width:326px;height:262px}
  .burst svg{position:absolute;inset:0;width:100%;height:100%}
  .burst__text{position:absolute;inset:0;display:flex;flex-direction:column;align-items:center;justify-content:center;font-family:"Oswald",sans-serif;color:var(--steel);line-height:1.02;text-shadow:1px 1px 0 var(--steel-deep);padding-bottom:10px}
  .burst__price{font-size:52px;font-weight:700}
  .burst__label{font-size:42px;font-weight:700}

  /* 20% off */
  .discount{left:289px;top:451px;width:348px;height:180px;border-radius:10px;background:linear-gradient(180deg,#eef3f6 0%,#b9ccd6 60%,#a4bccb 100%);border:2px solid var(--white);box-shadow:0 2px 6px rgba(0,0,0,.35);text-align:center;color:var(--steel)}
  .discount__big{font-size:58px;font-weight:900;color:var(--white);line-height:1;margin-top:8px;text-shadow:0 0 2px var(--steel-deep),2px 2px 0 var(--steel-deep)}
  .discount__line{font-family:"Oswald",sans-serif;font-size:32px;font-weight:700;line-height:1.05;text-shadow:1px 1px 0 var(--steel-deep)}
  .discount__note{font-size:16px;font-weight:700;margin-top:6px}

  /* call scroll */
  .call{left:245px;top:636px;width:500px;height:94px;background:var(--white);border-radius:6px 20px 6px 20px;text-align:center;box-shadow:0 1px 3px rgba(0,0,0,.2)}
  .call__lead{font-size:27px;font-weight:800;font-style:italic;color:var(--steel);margin-top:4px;letter-spacing:.5px}
  .call__phone{font-size:48px;font-weight:800;font-style:italic;color:var(--steel);letter-spacing:1px;line-height:1.05;text-shadow:1px 1px 0 var(--steel-deep)}

  /* brand */
  .brand{left:0;top:870px;width:1151px;text-align:center}
  .brand__mark{display:inline-flex;align-items:center;gap:22px}
  .brand__dot{width:46px;height:46px;border-radius:50%;background:var(--steel)}
  .brand__name{font-family:"Questrial",sans-serif;font-size:60px;color:var(--brown);line-height:1}
  .brand__tagline{font-family:"Questrial",sans-serif;font-size:28px;color:var(--brown);letter-spacing:2px;margin-top:70px}
  .site{left:0;top:1050px;width:1151px;text-align:center;font-size:44px;font-weight:800;color:var(--steel);text-shadow:1px 1px 0 var(--steel-deep),2px 3px 3px rgba(0,0,0,.3)}
  .slogan{left:0;top:1112px;width:1151px;text-align:center;font-size:34px;font-weight:900;color:var(--white);line-height:1.02;-webkit-text-stroke:1.5px var(--steel-deep);text-shadow:2px 2px 2px rgba(0,0,0,.4)}
</style>
</head>
<body>
<main class="ad">
  <svg class="ad__backdrop" viewBox="0 0 1151 1200">
    <defs>
      <linearGradient id="sky-left" x1="0" y1="0" x2="0" y2="1">
        <stop offset="0" stop-color="#ffffff"/>
        <stop offset="1" stop-color="#dfe6ec"/>
      </linearGradient>
      <linearGradient id="scene-tone" x1="0" y1="0" x2="1" y2="0">
        <stop offset="0" stop-color="#a9b8c6"/>
        <stop offset=".5" stop-color="#b7bdb9"/>
        <stop offset="1" stop-color="#5f7560"/>
      </linearGradient>
      <linearGradient id="tree-tone" x1="0" y1="0" x2="0" y2="1">
        <stop offset="0" stop-color="#8fb0c0" stop-opacity=".25"/>
        <stop offset="1" stop-color="#5a4840" stop-opacity=".15"/>
      </linearGradient>
    </defs>
    <rect width="1151" height="640" fill="url(#sky-left)"/>
    <rect x="515" y="0" width="636" height="600" fill="var(--teal-dark)"/>
    <rect role="img" aria-label="Stylised tree with soft blue leaves" x="300" y="40" width="420" height="520" fill="url(#tree-tone)"/>
    <rect role="img" aria-label="Snow-capped mountain landscape photo with pine forest" x="0" y="560" width="1151" height="250" fill="url(#scene-tone)"/>
    <path d="M0 820C250 760 560 720 800 745C960 762 1070 780 1151 770V810H0Z" fill="var(--white)"/>
    <path d="M0 800C250 745 560 712 800 735C960 752 1070 770 1151 760V790C1060 800 950 790 800 775C560 750 260 790 0 845Z" fill="var(--brown)"/>
    <rect y="830" width="1151" height="370" fill="var(--white)"/>
    <path d="M0 840L190 975L0 1065Z" fill="var(--grey-light)"/>
    <path d="M1151 820L965 975L1151 1065Z" fill="var(--grey)"/>
    <path d="M0 1065L190 975H965L1151 1065V1200H0Z" fill="var(--grey-light)"/>
    <path d="M0 1065L190 975H965L1151 1065" fill="none" stroke="#eeeeee" stroke-width="3"/>
  </svg>

  <section class="block providers">
    <h2 class="providers__title">Preferred Provider For:</h2>
    <p class="providers__list">Harbor Dental, Veridan Life, Northpoint, Solvane</p>
    <p class="providers__list providers__list--gap">Bluecrest and United Meridia</p>
    <p class="providers__note">We take all other non-HMO plans</p>
  </section>

  <section class="block referral">
    <div class="referral__card"></div>
    <div class="referral__card"></div>
    <div class="referral__card referral__card--front">
      <span class="referral__lead">Ask about our</span>
      <span class="referral__word">Referral</span>
      <span class="referral__word">Program</span>
    </div>
  </section>

  <section class="block newpatients">
    <h2 class="newpatients__title">$59 New patients</h2>
    <p class="newpatients__item">X-Rays</p>
    <p class="newpatients__item">Comprehensive Exam</p>
    <p class="newpatients__item">Regular Cleaning</p>
    <p class="newpatients__note">*Only patients without Dental Benefits</p>
  </section>

  <section class="block burst">
    <svg viewBox="0 0 318 262" preserveAspectRatio="none" aria-hidden="true">
      <polygon fill="#ffffff" points="159,0 180,62 230,12 222,78 300,52 256,108 318,130 256,150 304,208 228,190 232,255 180,200 159,262 138,200 86,255 90,190 14,208 62,150 0,130 62,108 18,52 96,78 88,12 138,62"/>
    </svg>
    <div class="burst__text">
      <span class="burst__price">$99</span>
      <span class="burst__label">Bleaching</span>
      <span class="burst__label">Special</span>
    </div>
  </section>

  <section class="block discount">
    <p class="discount__big">20% OFF</p>
    <p class="discount__line">Treatment scheduled</p>
    <p class="discount__line">on your first visit</p>
    <p class="discount__note">Only patients without Dental Benefits</p>
  </section>

  <section class="block call">
    <p class="call__lead">Call Today for an Appointment</p>
    <p class="call__phone">614-382-2096</p>
  </section>

  <section class="block brand">
    <div class="brand__mark">
      <span class="brand__dot"></span>
      <span class="brand__name">Larkmoor Dental Center</span>
    </div>
    <p class="brand__tagline">FAMILY • COSMETIC • IMPLANTS</p>
  </section>

  <p class="block site">www.larkmoordentalcenter.example</p>
  <p class="block slogan">WHERE THE WHOLE FAMILY<br>CAN BE SEEN!</p>
</main>
</body>
</html>
```